Hi Tech startup needs an investor presentation

We need an investor presentaiton for a new company based in Russia. We develop innovative solutions connecting customers and businesses via VoIP. Our initial product is an iPhone / Android app connecting customers directly to call centers / help desks bypassing calling (800) numbers. This also saves money for companies who do not need to pay for (800) lines.
Updates

Hi guys!

I have now made the contest committed, so please participate.

Industry/Entity Type

It Company

Requirements
Must have
• The ppt must follow the structure already suggested in the uploaded ppt
Nice to have
• Some nice graphic solutions, pictograms and so on instead of large chunks of text
Should not have
• Should not use old-style fonts and solutions.
• Also, not too cocky please.

```html
<!DOCTYPE html>
<html lang="en">
<head>
<meta charset="utf-8">
<title>Tonvia — Investor Presentation</title>
<link href="https://fonts.googleapis.com/css2?family=Arimo:wght@400;700&display=swap" rel="stylesheet">
<style>
:root{
  --orange:#f0902a;
  --orange-deep:#ee8420;
  --orange-light:#f7b230;
  --bar:#f6b434;
  --ring:#fbc93a;
  --ink:#2b2b2b;
  --text:#444;
  --muted:#fde0b0;
  --link:#d0245c;
  --axis:#2f8fd6;
  --page:#ffffff;
}
*{box-sizing:border-box;margin:0;padding:0}
html,body{width:1200px;height:1000px;overflow:hidden;background:var(--page);font-family:"Arimo",Arial,sans-serif;color:var(--text)}
.canvas{position:relative;width:1200px;height:1000px}
.heading{position:absolute;top:36px;left:0;width:100%;text-align:center;font-size:38px;color:var(--orange);font-weight:400}
.slide{position:absolute;width:372px;height:280px;background:#fff;overflow:hidden}
.slide.cover{background:linear-gradient(150deg,var(--orange-deep) 0%,var(--orange) 45%,var(--orange-light) 100%)}
.cover .arcs{position:absolute;inset:0}
.cover-title{position:absolute;left:22px;top:34px;font-size:16.5px;line-height:1.25;color:var(--ink)}
.cover-date{position:absolute;left:22px;font-size:6.5px;color:var(--muted)}
.brand{position:absolute;display:flex;align-items:center;gap:6px;color:#333;font-weight:400}
.brand .dot{border-radius:50%;background:var(--orange-light)}
.footer{position:absolute;left:0;bottom:0;width:100%;height:20px;background:var(--bar)}
.footer .brand{right:14px;top:5px;font-size:8px;gap:3px}
.footer .brand .dot{width:8px;height:8px;background:#fff}
.title{position:absolute;left:22px;top:38px;font-size:13.5px;line-height:1.2;color:var(--ink)}
.subtitle{font-size:8.5px;color:var(--orange-light);margin-top:3px}
.body{position:absolute;left:22px;right:18px;font-size:7.2px;line-height:1.3;color:var(--text)}
.body ul{list-style:none}
.body li{position:relative;padding-left:9px;margin-bottom:7px}
.body li::before{content:"•";position:absolute;left:0}
.body.tight li{margin-bottom:2px}
.group{color:var(--orange);font-weight:700;font-size:8.5px;margin:8px 0 3px}
.body b{color:#222}
.step{position:absolute;left:30px;display:flex;align-items:flex-start;gap:10px;width:330px}
.step-num{width:24px;height:24px;border-radius:50%;background:var(--orange-light);color:#fff;font-size:11px;display:flex;align-items:center;justify-content:center;flex:none}
.step-text{font-size:6.6px;line-height:1.3;width:170px;color:#333}
.step-text strong{font-weight:400;font-size:6.8px;display:block;margin:3px 0 2px;color:#222}
.step-text span{display:block;padding-left:6px}
.go{position:absolute;width:11px;height:11px;border-radius:50%;background:var(--orange-light)}
.go svg{display:block}
.visual{position:absolute;border-radius:4px}
.member{position:absolute;left:22px;font-size:5.6px;line-height:1.35;width:200px;color:#333}
.portrait{position:absolute;width:56px;height:48px;background:linear-gradient(160deg,#c9d3de,#7d8b99)}
.small{position:absolute;left:22px;font-size:5.4px;line-height:1.5;color:#333}
.chart{position:absolute;inset:0}
.chart text{font-family:"Arimo",Arial,sans-serif}
.contact{position:absolute;font-size:8px;color:#333;line-height:1.35}
.contact a{color:var(--link)}
</style>
</head>
<body>
<div class="canvas">
  <h1 class="heading">Sample Design</h1>

  <!-- Slide 1: cover -->
  <section class="slide cover" style="left:18px;top:103px">
    <svg class="arcs" width="372" height="280" viewBox="0 0 372 280" aria-hidden="true">
      <circle cx="392" cy="332" r="236" fill="var(--ring)"/>
      <circle cx="404" cy="340" r="216" fill="#fff"/>
    </svg>
    <h2 class="cover-title">Connecting businesses and<br>customers in a revolutionary way</h2>
    <p class="cover-date" style="top:78px">October 26, 2013</p>
    <div class="brand" style="left:218px;top:182px;font-size:30px"><span class="dot" style="width:34px;height:34px"></span>Tonvia</div>
  </section>

  <!-- Slide 2 -->
  <section class="slide" style="left:413px;top:103px">
    <h2 class="title">Who we are and what we believe</h2>
    <div class="body" style="top:68px">
      <ul>
        <li>St.-Petersburg-based developer and marketer of proprietary cloud-based VoIP solutions;</li>
        <li>We directly address the need for effective, efficient, cheap and easy communication between businesses and customers;</li>
        <li>We do not like the way corporation treat their customers, we are not happy with the way large telecom operators work, and we are not happy about corporate digital footprint and information, which is available to customers;</li>
        <li>We strongly believe that information has to be free and readily available to anyone with data connection and that communication has to be absolutely free and unchained.</li>
      </ul>
    </div>
    <div class="footer"><div class="brand"><span class="dot"></span>Tonvia</div></div>
  </section>

  <!-- Slide 3 -->
  <section class="slide" style="left:806px;top:103px">
    <h2 class="title" style="top:24px">Problem: both customers and businesses have<br>significant problems with “toll free” (800) numbers</h2>
    <div class="body tight" style="top:60px">
      <p class="group">Customers:</p>
      <ul>
        <li>Long waiting minutes – poor customer experience;</li>
        <li>Convoluted navigation, poor interactive voice response (IVR) – you always end up at the wrong desk and speak to the wrong person – even poorer customer experience.</li>
      </ul>
      <p class="group">Businesses:</p>
      <ul>
        <li>“Toll free” numbers are only free for the customers, as businesses in the United States pay up to $0.06 per minute on (800) numbers;</li>
        <li>10 customers are lost per each complaining client in the United States (Bizstat study);</li>
        <li>Poor IVR only makes it worse, as bills stack up and customers are dissatisfied.</li>
      </ul>
    </div>
    <div class="footer"><div class="brand"><span class="dot"></span>Tonvia</div></div>
  </section>

  <!-- Slide 4 -->
  <section class="slide" style="left:18px;top:404px">
    <h2 class="title" style="top:20px">Solution – mobile cloud-based business<br>phonebook</h2>
    <div class="body" style="top:62px;font-size:6.6px">
      <ul>
        <li><b>Find information about businesses</b> – simple Folder browser-style menu allowing you to browse industries / companies / departments / typical problems and <b>then connect</b> to the right person right away;</li>
        <li>Navigation is completed <b>before</b> the call is made;</li>
        <li>Shorter calls, <b>better customer experience;</b></li>
        <li>Shorter calls, <b>less phone bills</b> for the business;</li>
        <li>We operate telephony through our <b>own proprietary phone solution</b> based on Tonvia IP-PBX;</li>
        <li>VoIP means our minutes are actually <b>FREE</b> rather than traditional “toll free” minutes in exchange for as low as <b>$1 a month</b> per user (<b>25x-50x economy</b> depending on your price plan);</li>
        <li><b>Better customer experience</b> means <b>more sales</b>, and more <b>loyal customers</b>;</li>
        <li><b>Additional services</b> like calls from web / social networks / etc</li>
      </ul>
    </div>
    <div class="footer"><div class="brand"><span class="dot"></span>Tonvia</div></div>
  </section>

  <!-- Slide 5 -->
  <section class="slide" style="left:413px;top:404px">
    <h2 class="title" style="top:22px;font-size:16px">How does it work?<div class="subtitle">We guarantee the most user-friendly experience ever</div></h2>
    <div class="step" style="top:78px">
      <div class="step-num">1</div>
      <div class="step-text"><strong>Easy installation and set up process</strong><span>• Quick and easy;</span><span>• Free;</span><span>• SyncCore means no need to use your phone memory, the information is downloaded into your phone every time through cloud solutions</span></div>
    </div>
    <div class="step" style="top:142px">
      <div class="step-num">2</div>
      <div class="step-text"><strong>All the information you need is in your phone!</strong><span>• Listing-style content;</span><span>• Easy navigation between companies / departments;</span><span>• Problem evaluation forms to direct you to the right desk;</span><span>• One-click connection</span></div>
    </div>
    <div class="step" style="top:212px">
      <div class="step-num">3</div>
      <div class="step-text"><strong style="margin-top:8px">Start enjoying the time and money you have saved!</strong></div>
    </div>
    <span class="go" style="left:246px;top:106px"><svg width="11" height="11" viewBox="0 0 11 11"><path d="M4 3l3 2.5L4 8" stroke="#fff" stroke-width="1.3" fill="none"/></svg></span>
    <span class="go" style="left:246px;top:164px"><svg width="11" height="11" viewBox="0 0 11 11"><path d="M4 3l3 2.5L4 8" stroke="#fff" stroke-width="1.3" fill="none"/></svg></span>
    <span class="go" style="left:246px;top:224px"><svg width="11" height="11" viewBox="0 0 11 11"><path d="M4 3l3 2.5L4 8" stroke="#fff" stroke-width="1.3" fill="none"/></svg></span>
    <div class="visual" role="img" aria-label="Phone and laptop syncing with a cloud" style="left:270px;top:78px;width:84px;height:46px;background:linear-gradient(135deg,#dfeaf3,#9fb6c8)"></div>
    <div class="visual" role="img" aria-label="Two people calling each other through a cloud" style="left:268px;top:146px;width:88px;height:40px;background:linear-gradient(135deg,#e6eef5,#8fa6b8)"></div>
    <div class="visual" role="img" aria-label="Growth chart with devices" style="left:282px;top:200px;width:66px;height:44px;background:linear-gradient(135deg,#eef2f5,#a9b7c2)"></div>
    <div class="footer"><div class="brand"><span class="dot"></span>Tonvia</div></div>
  </section>

  <!-- Slide 6 -->
  <section class="slide" style="left:806px;top:404px">
    <h2 class="title" style="top:20px">Our Team is the Reason why we think<br>we will succeed</h2>
    <p class="body" style="top:64px;font-size:8.6px;line-height:1.3">Core Team presents a healthy mix of tech and business expertise and experience of life and mentality both in Russia and abroad:</p>
    <p class="member" style="top:100px"><b>Pavel Korinov, CEO, co-founder</b> – seasoned internet business leader (Findly MD) and strategist (ex-Cargo Line Head of Development and Northgate Advisory Managing Partner), City School of Economics graduate, Degrees in Law and Financial Management;</p>
    <p class="member" style="top:160px"><b>Oleg Marden, co-founder</b> – experienced telecom and IT entrepreneur with multiple projects in Telecom, IT, and Cleantech with a Degree in Secured communication channels;</p>
    <span class="go" style="left:248px;top:112px"><svg width="11" height="11" viewBox="0 0 11 11"><path d="M4 3l3 2.5L4 8" stroke="#fff" stroke-width="1.3" fill="none"/></svg></span>
    <span class="go" style="left:248px;top:172px"><svg width="11" height="11" viewBox="0 0 11 11"><path d="M4 3l3 2.5L4 8" stroke="#fff" stroke-width="1.3" fill="none"/></svg></span>
    <div class="portrait" role="img" aria-label="Portrait photo of the CEO" style="left:278px;top:96px"></div>
    <div class="portrait" role="img" aria-label="Portrait photo of the co-founder" style="left:278px;top:156px"></div>
    <p class="small" style="top:215px">Our engineers come from Ringhub, Netwave and<br>other leading VoIP and data companies;</p>
    <p class="small" style="top:235px">Our advisors come from the ranks of Ringhub, Telerus and Mobiline</p>
    <div class="footer"><div class="brand"><span class="dot"></span>Tonvia</div></div>
  </section>

  <!-- Slide 7 -->
  <section class="slide" style="left:18px;top:697px">
    <h2 class="title" style="top:26px;font-size:12.5px">We do not like clumsy solutions and large companies<br>reaping benefits for no reason</h2>
    <svg class="chart" width="372" height="280" viewBox="0 0 372 280" aria-label="Market positioning map">
      <defs><marker id="tip" markerWidth="6" markerHeight="6" refX="5" refY="3" orient="auto"><path d="M0 0L6 3L0 6z" fill="var(--axis)"/></marker></defs>
      <line x1="180" y1="225" x2="180" y2="80" stroke="var(--axis)" stroke-width="1.2" marker-end="url(#tip)"/>
      <line x1="80" y1="150" x2="318" y2="150" stroke="var(--axis)" stroke-width="1.2" marker-end="url(#tip)"/>
      <text x="172" y="72" font-size="6.5" fill="var(--orange)">Free</text>
      <text x="162" y="236" font-size="6.5" fill="var(--orange)">Expensive</text>
      <text x="28" y="152" font-size="6.5" fill="var(--orange)">No content</text>
      <text x="296" y="152" font-size="6.5" fill="var(--orange)">Useful content</text>
      <circle cx="96" cy="91" r="4" fill="#29a3dd"/><text x="103" y="94" font-size="8" font-weight="700" fill="#29a3dd">Talkly</text>
      <circle cx="96" cy="111" r="4" fill="#e06b2a"/><text x="103" y="114" font-size="8" font-weight="700" fill="#e06b2a">Ringhub</text>
      <circle cx="96" cy="130" r="4" fill="#7b4fa8"/><text x="103" y="133" font-size="8" font-weight="700" fill="#7b4fa8">Chatvibe</text>
      <circle cx="99" cy="167" r="4" fill="#3a3a3a"/><text x="106" y="170" font-size="8" font-weight="700" fill="#3a3a3a">Telnova</text>
      <circle cx="99" cy="190" r="4" fill="#c32026"/><text x="106" y="193" font-size="8" font-weight="700" fill="#c32026">Veritel</text>
      <circle cx="219" cy="111" r="4" fill="var(--orange-light)"/><text x="226" y="114" font-size="8" fill="#333">Tonvia</text>
      <circle cx="224" cy="180" r="4" fill="#d32323"/><text x="231" y="183" font-size="8" font-weight="700" fill="#333">Listo</text>
      <rect x="20" y="222" width="74" height="26" fill="#fff" stroke="#aaa" stroke-width="0.6"/>
      <text x="26" y="232" font-size="5.6" fill="#333">Business info</text>
      <line x1="72" y1="230" x2="86" y2="230" stroke="var(--axis)" stroke-width="1" marker-end="url(#tip)"/>
      <text x="26" y="243" font-size="5.6" fill="#333">Phone solutions</text>
      <line x1="82" y1="246" x2="82" y2="236" stroke="var(--axis)" stroke-width="1" marker-end="url(#tip)"/>
    </svg>
    <div class="footer"><div class="brand"><span class="dot"></span>Tonvia</div></div>
  </section>

  <!-- Slide 8 -->
  <section class="slide" style="left:413px;top:697px">
    <h2 class="title" style="top:24px">Looking forward to hearing from you and<br>thank you for your time!</h2>
    <p class="contact" style="left:118px;top:74px;text-align:center;font-size:9px">Pavel Korinov,<br>Co-founder</p>
    <div role="img" aria-label="Email" style="position:absolute;left:74px;top:120px;width:34px;height:28px;border-radius:3px;background:#e04a3a"></div>
    <p class="contact" style="left:134px;top:128px"><a>p.korinov@mailbox.example</a></p>
    <div role="img" aria-label="Messenger" style="position:absolute;left:76px;top:175px;width:30px;height:30px;border-radius:50%;background:#2aa5e0"></div>
    <p class="contact" style="left:134px;top:180px">pavel.korinov<br>+7 900 000 12 34<br>+7 900 000 56 78</p>
    <div class="footer"><div class="brand"><span class="dot"></span>Tonvia</div></div>
  </section>

  <!-- Slide 9: closing -->
  <section class="slide cover" style="left:806px;top:697px">
    <svg class="arcs" width="372" height="280" viewBox="0 0 372 280" aria-hidden="true">
      <circle cx="392" cy="332" r="236" fill="var(--ring)"/>
      <circle cx="404" cy="340" r="216" fill="#fff"/>
    </svg>
    <h2 class="cover-title" style="top:44px;font-size:11px">Thank You</h2>
    <p class="cover-date" style="top:64px">October 26, 2013</p>
    <div class="brand" style="left:216px;top:180px;font-size:30px"><span class="dot" style="width:34px;height:34px"></span>Tonvia</div>
  </section>
</div>
</body>
</html>
```